Photography business - business card design quick turn around

Create a business card design for me please. I actually need the final design back before the end of Sunday 13th May 7pm GMT. Sorry for the short notice.

Photoshop artwork template uploaded with artwork guidelines including printer profiles and other mandatory specifications. Only one side of the business card is required as the other side will be an image.

The design is required as an unflattened PSD file so that I can edit the text if I need to.

My brand colours are white and the teal you see in the logo. Occasionally I also use a dark grey on my website (I don't mind the shade of grey as appreciate grey on teal would be a different grey, to the grey I use on white on the website, so just use a shade of grey that matches). Font can be as the font for the logo or if you prefer I am open to another sans serif, easily legible font. Ideally font size will be 12+.Please do not use capital letters for text. I prefer everything to be lower case, if possible.

Thank you.

Nell

Target Market(s)

Other business owners who may refer me and families

Industry/Entity Type

Photographer

Contact Information for Business Card

Silver Kettle Photography Logo
Sub text: family portraiture, captured with love

Contact information, ideally using simple icons to represent email / website / facebook / instagram / pinterest

email: nell@silverkettlephotography.co.uk
website: silverkettlephotography.co.uk
facebook: @silverkettlephotography
pinterest: pinterest.com/silverkettlepho
instagram: @silverkettle_photography
mobile/telephone: 07931462097

If there is too much text then please drop the instagram and pinterest information.

Font styles to use
Sans Serif

Colors
33b8a4

Requirements
Must have
• Logo
• Contact details as listed above
• sub text
Nice to have
• Instagram and Pinterest contact details
• Nice to have icons to represent website / phone / facebook etc followered by the handle where relevant

```html
<!DOCTYPE html>
<html lang="en">
<head>
<meta charset="utf-8">
<title>Silver Kettle Photography – business card</title>
<link rel="stylesheet" href="https://fonts.googleapis.com/css2?family=Arimo:wght@400&family=Questrial&family=Tinos:ital@1&display=swap">
<style>
  :root {
    --page-bg: #2b2b2d;
    --teal: #33b8a4;
    --teal-dark: #279483;
    --photo-mid: #9a9795;
    --photo-edge: #737170;
    --face-light: #ffffff;
    --face-shade: #dcdcdc;
    --ink: #3a3a3a;
    --ink-soft: #5f5f5f;
    --white: #ffffff;
  }
  * { box-sizing: border-box; margin: 0; padding: 0; }
  html, body { width: 1200px; height: 997px; overflow: hidden; }
  body {
    background: var(--page-bg);
    font-family: "Arimo", Arial, sans-serif;
    position: relative;
  }
  .card {
    position: absolute;
    left: 240px;
    width: 720px;
    height: 411px;
    border-radius: 22px;
    overflow: hidden;
    box-shadow: 0 14px 30px rgba(0,0,0,.45);
  }

  /* front */
  .card--front { top: 48px; }
  .front-photo {
    position: absolute; inset: 0;
    background: radial-gradient(ellipse at 62% 45%, var(--photo-mid) 0%, #8a8785 45%, var(--photo-edge) 100%);
  }
  .front-brand {
    position: absolute; left: 40px; bottom: 70px;
    display: flex; align-items: center; gap: 12px;
    font-family: "Questrial", sans-serif;
    font-size: 22px; color: var(--white); text-transform: lowercase;
  }
  .brand-dot { width: 16px; height: 16px; border-radius: 50%; background: currentColor; flex: none; }

  /* back */
  .card--back {
    top: 538px;
    background: linear-gradient(170deg, var(--face-light) 30%, var(--face-shade) 100%);
  }
  .tagline-band {
    position: absolute; top: 0; left: 0; right: 0; height: 70px;
    background: linear-gradient(180deg, var(--teal), var(--teal-dark));
    display: flex; align-items: center; justify-content: center;
    font-family: "Tinos", serif; font-style: italic;
    font-size: 30px; color: var(--white); letter-spacing: .5px;
  }
  .foot-band {
    position: absolute; bottom: 0; left: 0; right: 0; height: 24px;
    background: var(--teal-dark);
  }
  .back-brand {
    position: absolute; top: 118px; left: 0; right: 0;
    display: flex; align-items: center; justify-content: center; gap: 16px;
    font-family: "Questrial", sans-serif;
    font-size: 40px; color: var(--ink-soft); text-transform: lowercase;
  }
  .back-brand .brand-dot { width: 18px; height: 18px; background: var(--teal); }

  .contact-list, .social-list {
    position: absolute;
    list-style: none; display: grid; gap: 10px;
    font-size: 18px; color: var(--ink);
  }
  .contact-list { left: 30px; bottom: 42px; }
  .social-list { right: 30px; top: 222px; }
  .contact-list li, .social-list li { display: flex; align-items: center; gap: 12px; white-space: nowrap; }
  .social-list li { justify-content: flex-end; }
  .icon { width: 24px; height: 24px; flex: none; }
  .icon-bg { fill: var(--teal); }
</style>
</head>
<body>

<section class="card card--front" aria-label="card front">
  <div class="front-photo" role="img" aria-label="studio portrait of a toddler in a denim jacket posed on a grey backdrop"></div>
  <div class="front-brand"><span class="brand-dot"></span>silver kettle photography</div>
</section>

<section class="card card--back" aria-label="card back">
  <div class="tagline-band">family portraiture, captured with love</div>

  <div class="back-brand"><span class="brand-dot"></span>silver kettle photography</div>

  <ul class="social-list">
    <li>silverkettlephotography
      <svg class="icon" viewBox="0 0 24 24" aria-label="social page"><circle class="icon-bg" cx="12" cy="12" r="12"/><circle cx="12" cy="9" r="3" fill="#fff"/><path d="M6.5 17.5a5.5 5.5 0 0 1 11 0z" fill="#fff"/></svg>
    </li>
    <li>silverkettlepho
      <svg class="icon" viewBox="0 0 24 24" aria-label="boards"><circle class="icon-bg" cx="12" cy="12" r="12"/><path d="M8 6h8v12l-4-3-4 3z" fill="#fff"/></svg>
    </li>
    <li>silverkettle_photography
      <svg class="icon" viewBox="0 0 24 24" aria-label="handle"><circle class="icon-bg" cx="12" cy="12" r="12"/><circle cx="12" cy="12" r="2.6" fill="none" stroke="#fff" stroke-width="1.6"/><path d="M14.6 12v1.2a1.8 1.8 0 0 0 3.6 0V12a6.2 6.2 0 1 0-2.4 4.9" fill="none" stroke="#fff" stroke-width="1.6" stroke-linecap="round"/></svg>
    </li>
  </ul>

  <ul class="contact-list">
    <li>
      <svg class="icon" viewBox="0 0 24 24" aria-hidden="true"><circle class="icon-bg" cx="12" cy="12" r="12"/><path d="M8 7h2l1 3-1.5 1a7 7 0 0 0 3.5 3.5l1-1.5 3 1v2a1.5 1.5 0 0 1-1.5 1.5A9 9 0 0 1 6.5 8.5 1.5 1.5 0 0 1 8 7z" fill="#fff"/></svg>
      07931462097
    </li>
    <li>
      <svg class="icon" viewBox="0 0 24 24" aria-hidden="true"><circle class="icon-bg" cx="12" cy="12" r="12"/><rect x="6" y="8" width="12" height="8" rx="1" fill="#fff"/><path d="M6.5 8.5l5.5 4 5.5-4" fill="none" stroke="var(--teal)" stroke-width="1.2"/></svg>
      nell@silverkettlephotography.co.uk
    </li>
    <li>
      <svg class="icon" viewBox="0 0 24 24" aria-hidden="true"><circle class="icon-bg" cx="12" cy="12" r="12"/><path d="M12 5a4.5 4.5 0 0 1 4.5 4.5c0 3.5-4.5 9-4.5 9s-4.5-5.5-4.5-9A4.5 4.5 0 0 1 12 5z" fill="#fff"/><circle cx="12" cy="9.5" r="1.7" fill="var(--teal)"/></svg>
      silverkettlephotography.co.uk
    </li>
  </ul>

  <div class="foot-band"></div>
</section>

</body>
</html>
```